Fresh, modern, fun business card for pediatric dental practice

Need a business card for fresh, modern, fun pediatric dental practice

Clean look that matches our website's font and colors

We prefer the look of curved corners on business cards

Target Market(s)

parents (mothers) of young children, professionals, mid-high class

Industry/Entity Type

Dental

Contact Information for Business Card

Maplebrook Pediatric Dentistry
482 Orchard Vale Road
Suite 517
Fernhaven, PA 19402
555.419.3067
www.maplebrookkidsdental.example

Mara Tevlin, DMD
Colette Varnum, DMD
(we are working on our email address, but we would like that on the card as well)

Font styles to use
Sans Serif

Requirements
Must have
• All info; we would also like to make cards for individual staff members
• colors from our website and color palatte, attatched
• use same font and design as website for branding
Nice to have
• clean, simple card that has a pop of color
• we would like to see a few designs with our tag line "where smiles get brighter"
• we are not sure if we want to have it on there or not
• we would like to see a few designs incorporating the ribbon graphic on our website where the word WELCOME is

```html
<!DOCTYPE html>
<html lang="en">
<head>
<meta charset="utf-8">
<title>Maplebrook Pediatric Dentistry – Business Card</title>
<link href="https://fonts.googleapis.com/css2?family=Ubuntu:wght@300;400;500;700&family=Roboto:wght@400&display=swap" rel="stylesheet">
<style>
  :root {
    --plum: #4b2d4a;
    --gold: #e0a100;
    --magenta: #b8177c;
    --ink: #2d2d2d;
    --paper: #f7f7f6;
    --backdrop: #e4e4e4;
    --soft-white: #ece6eb;
  }
  * { box-sizing: border-box; margin: 0; padding: 0; }
  html, body {
    width: 1200px; height: 576px; overflow: hidden;
    background: var(--backdrop);
  }
  .canvas { position: relative; width: 1200px; height: 576px; }

  .card {
    position: absolute; top: 138px;
    width: 484px; height: 292px;
    border-radius: 14px;
    overflow: hidden;
  }

  /* Front */
  .card-front { left: 82px; background: var(--plum); }
  .card-front .name-main {
    position: absolute; left: 0; right: 0; top: 134px;
    text-align: center;
    font-family: "Ubuntu", sans-serif; font-weight: 700;
    font-size: 46px; line-height: 46px; letter-spacing: 1.5px;
    color: var(--gold);
  }
  .card-front .name-sub {
    position: absolute; left: 0; right: 0; top: 182px;
    text-align: center;
    font-family: "Ubuntu", sans-serif; font-weight: 300;
    font-size: 24px; line-height: 24px; letter-spacing: 1.8px;
    color: var(--soft-white);
  }
  .card-front .web-line {
    position: absolute; left: 0; right: 0; top: 264px;
    display: flex; align-items: center; justify-content: center; gap: 22px;
    font-family: "Roboto", sans-serif; font-size: 12px; line-height: 14px;
    color: var(--soft-white); letter-spacing: 0.6px;
  }
  .card-front .web-line .rule {
    width: 56px; height: 2px; background: var(--magenta); border-radius: 1px;
  }
  .card-front .web-line .domain { color: var(--gold); }

  /* Back */
  .card-back { left: 602px; background: var(--paper); }
  .card-back .name-main {
    position: absolute; left: 18px; top: 33px;
    font-family: "Ubuntu", sans-serif; font-weight: 700;
    font-size: 32px; line-height: 32px; letter-spacing: 1px;
    color: var(--gold);
  }
  .card-back .name-sub {
    position: absolute; left: 19px; top: 65px;
    font-family: "Ubuntu", sans-serif; font-weight: 400;
    font-size: 17px; line-height: 17px; letter-spacing: 1.2px;
    color: var(--magenta);
  }

  .doctor-name {
    position: absolute; left: 19px; top: 159px;
    font-family: "Ubuntu", sans-serif; font-weight: 700;
    font-size: 16px; line-height: 18px; color: var(--gold);
  }
  .address {
    position: absolute; left: 19px; top: 186px;
    font-family: "Roboto", sans-serif; font-size: 12.8px; line-height: 17px;
    color: var(--ink); font-style: normal;
  }
  .contact-list {
    position: absolute; left: 19px; top: 226px;
    list-style: none;
    font-family: "Roboto", sans-serif; font-size: 12.8px; line-height: 16.8px;
    color: var(--ink);
  }
  .contact-list li { display: flex; align-items: center; gap: 8px; }
  .contact-list svg { width: 10px; height: 10px; fill: var(--magenta); flex: none; }
  .contact-list .domain { color: var(--magenta); }
</style>
</head>
<body>
<main class="canvas">

  <section class="card card-front" aria-label="Card front">
    <h1>
      <span class="name-main">maplebrook</span>
      <span class="name-sub">pediatric dentistry</span>
    </h1>
    <p class="web-line">
      <span class="rule"></span>
      <span>www.<span class="domain">maplebrookkidsdental</span>.example</span>
      <span class="rule"></span>
    </p>
  </section>

  <section class="card card-back" aria-label="Card back">
    <h2>
      <span class="name-main">maplebrook</span>
      <span class="name-sub">pediatric dentistry</span>
    </h2>
    <p class="doctor-name">Colette Varnum, DMD</p>
    <address class="address">
      482 Orchard Vale Road<br>
      Suite 517 Fernhaven, PA 19402
    </address>
    <ul class="contact-list">
      <li>
        <svg viewBox="0 0 10 10" aria-hidden="true"><path d="M1 3.2C1 2 2.5 1 5 1s4 1 4 2.2V4H7V3H3v1H1zM2.2 4.6h5.6L9 8.5H1z"/></svg>
        555.419.3067
      </li>
      <li>
        <svg viewBox="0 0 10 10" aria-hidden="true"><path d="M0.5 2h9v6h-9z M1 2.5L5 5.6 9 2.5" stroke="#f7f7f6" stroke-width="0.8"/></svg>
        name@maplebrookkidsdental.example
      </li>
      <li>
        <svg viewBox="0 0 10 10" aria-hidden="true"><circle cx="5" cy="5" r="4.5"/><path d="M0.5 5h9M5 0.5v9M2 2.5h6M2 7.5h6" stroke="#f7f7f6" stroke-width="0.7" fill="none"/></svg>
        <span>www.<span class="domain">maplebrookkidsdental</span>.example</span>
      </li>
    </ul>
  </section>

</main>
</body>
</html>
```